Homepage für Unternehmensberatung
Zielgruppe
Wir sind eine Unternehmensberatung mit einem klaren Branchenfokus auf Banken / Finanzdienstleister.
Unsere Dienstleistungsprodukte lassen sich grob in folgende Themencluster unterteilen:
1)Strategieentwicklung
o IT-Strategie, IT-Architektur, IT-Bebauungsplan
2) Projektmanagement
o Projektportfoliomgmt., Programmmgmt., Projektmanagement, Projektcontrolling
3) Fachberatung
o Bankfachliche IT- Beratung mit Schwerpunkten Kredit, Wertpapiergeschäft,
Bankenaufsichtsrecht, Liquiditätsmanagement
o Anforderungsmanagement inkl. Aufbau von Bewertungs- und Priorisierungsmethoden
4) Prozessberatung/-optimierung
o Prozessanalyse, Prozessdesign, Prozessdokumentation
o Prozessoptimierung auf Basis etablierter Messmethoden
Unser Firmenname Lindenhofer hat für uns eine Doppelbedeutung:
1. Im Außenverhältnis: Wir verstehen uns als Lindenhofer unserer Kunden
2. Im Innenverhältnis: Wir pflegen einen partnerschaftlichen Umgang mit unseren
Mitarbeitern (Teamarbeit)
Aktuell sind wir ein kleines aber feines Team von erfahrenen und hochmotivierten Kollegen. Unsere Mitarbeiter sind ehemalige Führungskräfte sowie erfahrenen Unternehmensberater.
Aufgabenstellung
Entwurf / Design von 2 Seiten:
1. Seite / Startseite:
Simple und elegante Darstellung der oben genannten 4 Themencluster (z.B. Bild/Piktogramm, Textkasten) sowie einer Navigationsmöglichkeit zu folgenden Detailsichten:
• Unternehmen
• Beratungsangebot (siehe Themencluster)
• Partnerunternehmen
• Kontakt
2. Seite / 2. Ebene:
Entwurf einer Möglichkeit zur Erläuterung/Darstellung von Inhalten der Startseite.
Die Themencluster sollten auf jeder Ebene immer „anklickbar“/ zu sehen sein.
Logo
Das angehängte Logo ist in die Website einzubinden. Stil und Farben sollen übernommen werden bzw. sind Basis für das Design.
Lizenzen
Lizenz für eingesetzte Fotos und Illustrationen soll enthalten / Open-Source sein. Wenn nicht dann bitte zusätzliche Kosten angeben.

```html
<!DOCTYPE html>
<html lang="de">
<head>
<meta charset="utf-8">
<title>Lindenhofer – Management- und Prozessberatung</title>
<link href="https://fonts.googleapis.com/css2?family=Ubuntu:wght@300;400;500&display=swap" rel="stylesheet">
<style>
:root{
  --blue:#1b7cb8;
  --blue-light:#2f9ad6;
  --blue-nav:#3a9bde;
  --blue-active:#2a7fb5;
  --text:#3c3c3c;
  --text-soft:#5b6168;
  --header-bg:#f7f7f7;
  --section-bg:#f3f3f3;
  --card-border:#e2e2e2;
  --btn-grey:#a3a3a3;
  --footer-bg:#3a3a3a;
  --footer-text:#9a9a9a;
  --footer-head:#c4c4c4;
  --icon:#6b6b6b;
}
*{margin:0;padding:0;box-sizing:border-box}
html,body{width:1171px;height:1200px;overflow:hidden}
body{position:relative;background:var(--section-bg);font-family:"Ubuntu",sans-serif;color:var(--text)}
.abs{position:absolute}

.top-strip{left:0;top:0;width:1171px;height:15px;background:#fff}
.site-header{left:0;top:15px;width:1171px;height:102px;background:var(--header-bg);border-bottom:1px solid #e4e4e4}
.brand{left:231px;top:41px;display:flex;align-items:center;gap:8px}
.brand-mark{width:44px;height:44px;border-radius:50%;background:var(--blue)}
.brand-name{font-size:21px;font-weight:400;color:var(--blue);letter-spacing:.5px;line-height:1}
.brand-tag{font-size:6px;letter-spacing:1.6px;color:#8a8f94;margin-top:5px}
.main-nav{left:545px;top:49px;width:416px;height:30px;background:var(--blue-nav);display:flex;align-items:center}
.main-nav a{color:#fff;text-decoration:none;font-size:9.5px;font-weight:500;height:30px;line-height:30px;padding:0 13px}
.main-nav a.active{background:var(--blue-active);padding:0 10px 0 13px;margin-right:9px}

.hero{left:0;top:117px;width:1171px;height:178px;background:#fff;box-shadow:0 6px 14px rgba(0,0,0,.08)}
.hero-title{left:238px;top:54px;font-size:21.5px;font-weight:400;color:#5e666d;line-height:27px}
.hero-title mark{background:#e3e6e9;color:var(--blue);padding:0 5px}
.hero-sub{left:238px;top:110px;font-size:12.5px;color:var(--blue)}
.hero-photo{left:721px;top:100px;width:163px;height:195px;background:linear-gradient(180deg,#dfe3e8 0%,#7d95b4 40%,#2e4e80 100%);border-radius:70px 70px 0 0}

.service{width:180px;text-align:center;top:340px}
.service svg{display:block;margin:0 auto;height:60px}
.service h2{font-size:14px;font-weight:500;color:var(--blue);margin-top:30px}
.service h3{font-size:11.5px;font-weight:400;color:var(--text);margin-top:9px}
.service p{font-size:9.6px;line-height:13.4px;margin-top:14px;color:var(--text)}
.btn-grey{display:inline-block;width:71px;height:24px;line-height:24px;background:var(--btn-grey);color:#fff;font-size:9px;margin-top:26px;border-bottom:1px solid #8d8d8d}

.divider{left:200px;top:607px;width:800px;height:1px;background:linear-gradient(90deg,transparent,#bdbdbd 30%,#bdbdbd 70%,transparent)}

.news-card{top:642px;width:223px;height:321px;background:#fff;border:1px solid var(--card-border);border-radius:3px}
.news-img{left:13px;top:16px;width:198px;height:119px}
.news-card h2{left:17px;top:160px;font-size:15px;font-weight:400;color:var(--blue-light)}
.news-card h3{left:17px;top:185px;font-size:11.5px;font-weight:400;color:var(--text)}
.news-card p{left:17px;top:211px;width:195px;font-size:9.6px;line-height:13.4px}
.btn-blue{left:15px;top:271px;width:90px;height:31px;line-height:31px;text-align:center;background:var(--blue-light);color:#fff;font-size:9px}

.site-footer{left:0;top:1014px;width:1171px;height:186px;background:var(--footer-bg)}
.footer-head{font-size:12px;color:var(--footer-head);font-weight:300;top:25px}
.footer-rule{top:51px;width:72px;height:1px;background:#666}
.footer-text{font-size:8px;line-height:13.4px;color:var(--footer-text)}
.social{top:129px;width:28px;height:28px;background:#6a6a6a}
.blog-item{left:397px;display:flex;gap:9px}
.blog-item svg{flex:none;margin-top:2px}
.badge{left:590px;top:66px;width:105px;height:37px;border-radius:4px;background:#555}
</style>
</head>
<body>
<div class="abs top-strip"></div>

<header class="abs site-header">
  <div class="abs brand">
    <div class="brand-mark"></div>
    <div>
      <div class="brand-name">LINDENHOFER</div>
      <div class="brand-tag">MANAGEMENT- UND PROZESSBERATUNG</div>
    </div>
  </div>
  <nav class="abs main-nav" style="top:34px">
    <a class="active" href="#">HOME</a>
    <a href="#">BERATUNGSANGEBOT</a>
    <a href="#">PARTNERUNTERNEHMEN</a>
    <a href="#">KONTAKT</a>
  </nav>
</header>

<section class="abs hero">
  <h1 class="abs hero-title">Nachhaltig planen. Efffizient umsetzen.<br>Mit der <mark>Kompetenz</mark> von Lindenhofer.</h1>
  <div class="abs hero-sub">Speziell für Banken &amp; Finanzdienstleister</div>
</section>
<div class="abs hero-photo" role="img" aria-label="Foto eines Beraters im blauen Anzug mit verschränkten Armen"></div>

<section>
  <div class="abs service" style="left:221px">
    <svg viewBox="0 0 60 60" fill="none" stroke="var(--icon)" stroke-width="3"><circle cx="30" cy="33" r="22"/><path d="M30 19v15h-12"/><path d="M12 12a8 8 0 0 1 10-4M48 12a8 8 0 0 0-10-4" stroke-width="4"/></svg>
    <h2>Strategieentwicklung</h2><h3>Hier steht die Subheadline</h3>
    <p>Aenean commodo ligula eget dolor. Aenean massa. Cum sociis natoque pgenatibus et magnis dis parturient mongtes, nascetur ridiculus mus.</p>
    <span class="btn-grey">weiter</span>
  </div>
  <div class="abs service" style="left:408px">
    <svg viewBox="0 0 60 60"><circle cx="25" cy="14" r="10" fill="none" stroke="var(--icon)" stroke-width="3"/><path d="M21 14v24l-5-5-4 3 9 14c2 3 4 5 8 5h8c4 0 6-3 6-7V34c0-3-2-4-4-4h-8V14a4 4 0 0 0-10 0z" fill="var(--icon)"/></svg>
    <h2>Fachberatung</h2><h3>Hier steht die Subheadline</h3>
    <p>Aenean commodo ligula eget dolor. Aenean massa. Cum sociis natoque pgenatibus et magnis dis parturient mongtes, nascetur ridiculus mus.</p>
    <span class="btn-grey">weiter</span>
  </div>
  <div class="abs service" style="left:592px">
    <svg viewBox="0 0 60 60" fill="none" stroke="var(--icon)" stroke-width="3"><path d="M10 44h40a8 8 0 0 0 0-16 12 12 0 0 0-22-6 9 9 0 0 0-14 7 7.5 7.5 0 0 0-4 15z"/></svg>
    <h2>Projektmanagement</h2><h3>Hier steht die Subheadline</h3>
    <p>Aenean commodo ligula eget dolor. Aenean massa. Cum sociis natoque pgenatibus et magnis dis parturient mongtes, nascetur ridiculus mus.</p>
    <span class="btn-grey">weiter</span>
  </div>
  <div class="abs service" style="left:786px">
    <svg viewBox="0 0 60 60" fill="none" stroke="var(--icon)" stroke-width="3"><circle cx="30" cy="30" r="26"/><ellipse cx="30" cy="30" rx="11" ry="26"/><path d="M30 4v52M4 30h52M8 17h44M8 43h44"/></svg>
    <h2>Prozessoptimierung</h2><h3>Hier steht die Subheadline</h3>
    <p>Aenean commodo ligula eget dolor. Aenean massa. Cum sociis natoque pgenatibus et magnis dis parturient mongtes, nascetur ridiculus mus.</p>
    <span class="btn-grey">weiter</span>
  </div>
</section>

<div class="abs divider"></div>

<section>
  <article class="abs news-card" style="left:220px">
    <div class="abs news-img" role="img" aria-label="Finanzchart mit Kursverläufen auf dunkelblauem Grund" style="background:linear-gradient(135deg,#06222f,#0d5a7a 55%,#062530)"></div>
    <h2 class="abs">News-Headline</h2><h3 class="abs">Hier steht die Subheadline</h3>
    <p class="abs">Aenean commodo ligula eget dolor. Aenean massa. Cum sociis natoque pgenatibus et magnis dis parturient</p>
    <span class="abs btn-blue">weiter</span>
  </article>
  <article class="abs news-card" style="left:483px">
    <div class="abs news-img" role="img" aria-label="Team bespricht Ideen an einer Glaswand" style="background:linear-gradient(90deg,#cfd9df,#b8c4cb 50%,#8c8f93)"></div>
    <h2 class="abs">News-Headline</h2><h3 class="abs">Hier steht die Subheadline</h3>
    <p class="abs">Aenean commodo ligula eget dolor. Aenean massa. Cum sociis natoque pgenatibus et magnis dis parturient</p>
    <span class="abs btn-blue">weiter</span>
  </article>
  <article class="abs news-card" style="left:747px">
    <div class="abs news-img" role="img" aria-label="Person zeichnet ein Ablaufdiagramm" style="background:linear-gradient(90deg,#d8cfc9,#f2f2f2 60%,#e8e8e8)"></div>
    <h2 class="abs">News-Headline</h2><h3 class="abs">Hier steht die Subheadline</h3>
    <p class="abs">Aenean commodo ligula eget dolor. Aenean massa. Cum sociis natoque pgenatibus et magnis dis parturient</p>
    <span class="abs btn-blue">weiter</span>
  </article>
</section>

<footer class="abs site-footer">
  <div class="abs footer-head" style="left:220px">Lindenhofer inside</div>
  <div class="abs footer-rule" style="left:220px"></div>
  <p class="abs footer-text" style="left:220px;top:71px;width:170px">Consectetur adipiscing elit aeneane lorem lipsum, condimentum ultrices conse-quatvehicula mauris lipsum adipiscing lipsum aenean orci lorem. onsequatv</p>
  <div class="abs social" style="left:220px"></div>
  <div class="abs social" style="left:256px"></div>
  <div class="abs social" style="left:291px"></div>
  <div class="abs social" style="left:327px"></div>

  <div class="abs footer-head" style="left:397px">Neues aus dem Blog</div>
  <div class="abs footer-rule" style="left:397px"></div>
  <div class="abs blog-item" style="top:71px">
    <svg width="12" height="14" viewBox="0 0 12 14" fill="none" stroke="#8a8a8a"><path d="M1 1h7l3 3v9H1z"/><path d="M3 6h6M3 8h6M3 10h6"/></svg>
    <p class="footer-text">I will be very restpsoon result recotio.<br>Ase result recotio soon result.<br>23 minutes ago</p>
  </div>
  <div class="abs blog-item" style="top:119px">
    <svg width="12" height="14" viewBox="0 0 12 14" fill="none" stroke="#8a8a8a"><path d="M1 1h7l3 3v9H1z"/><path d="M3 6h6M3 8h6M3 10h6"/></svg>
    <p class="footer-text">I will be very restpsoon result recotio.<br>Ase result recotio soon result.<br>23 minutes ago</p>
  </div>

  <div class="abs footer-head" style="left:580px">Partner</div>
  <div class="abs footer-rule" style="left:583px"></div>
  <div class="abs badge"></div>
</footer>
</body>
</html>
```